Bramble Bunnies Business Cards

I need a business card for my new Company called Bramble Bunnies. We create handmade baby moccasins, headbands, t-shirts and more. I want some that will appeal to parents, and to go with the colors of my logo that I have attached. feel free to be creative. I would like my logo placed somewhere on the card.

Industry/Entity Type

Retail

Contact Information for Business Card

Bramble Bunnies
20418 Wexley C #5127
Irvine Ca 92687
Rosalind Hatchett Ceo
Info@Bramble-Bunnies.com
www.Bramble-Bunnies.com
Phone 9495817302

Requirements
Nice to have
• Logo included

```html
<!DOCTYPE html>
<html lang="en">
<head>
<meta charset="utf-8">
<title>Bramble Bunnies Business Cards</title>
<link rel="stylesheet" href="https://fonts.googleapis.com/css2?family=Comic+Neue:wght@400;700&family=Mulish:ital,wght@0,400;0,600;1,400&display=swap">
<style>
  :root {
    --backdrop: #33424a;
    --orange: #ef7d55;
    --orange-deep: #8f4428;
    --brown: #8a4429;
    --ink: #141414;
    --paper: #ffffff;
    --faint: #ececec;
  }
  * { box-sizing: border-box; margin: 0; padding: 0; }
  html, body { width: 1200px; height: 1000px; overflow: hidden; }
  body {
    background: var(--backdrop);
    font-family: "Mulish", sans-serif;
    position: relative;
  }
  .card {
    position: absolute;
    left: 250px;
    width: 700px;
    height: 400px;
    overflow: hidden;
    box-shadow: 0 10px 30px rgba(0,0,0,0.35);
  }
  /* Front face */
  .card-front {
    top: 60px;
    background: linear-gradient(180deg, var(--orange) 0%, var(--orange-deep) 100%);
    color: var(--paper);
    text-align: center;
  }
  .front-mark {
    display: block;
    width: 56px;
    height: 56px;
    margin: 90px auto 22px;
    background: var(--paper);
    border-radius: 8px;
  }
  .front-name {
    font-family: "Comic Neue", cursive;
    font-weight: 400;
    font-size: 58px;
    line-height: 1;
  }
  .front-web {
    margin-top: 52px;
    font-size: 14px;
    letter-spacing: 0.3px;
  }
  /* Back face */
  .card-back {
    top: 540px;
    background: var(--paper);
    color: var(--ink);
  }
  .back-watermark {
    position: absolute;
    right: 90px;
    top: 30px;
    width: 190px;
    height: 190px;
    background: var(--faint);
    border-radius: 18px;
    opacity: 0.7;
  }
  .brand {
    position: absolute;
    left: 60px;
    top: 36px;
    text-align: center;
  }
  .brand-mark {
    display: block;
    width: 52px;
    height: 52px;
    margin: 0 auto 14px;
    background: var(--ink);
    border-radius: 6px;
  }
  .brand-name {
    font-family: "Comic Neue", cursive;
    font-weight: 700;
    font-size: 44px;
    line-height: 1;
    color: var(--ink);
  }
  .contact-list {
    position: absolute;
    left: 52px;
    top: 222px;
    list-style: none;
    font-size: 15px;
    font-style: italic;
  }
  .contact-item {
    display: flex;
    align-items: center;
    gap: 12px;
    height: 27px;
  }
  .contact-item svg { width: 16px; height: 16px; fill: var(--orange); flex: none; }
  .person {
    position: absolute;
    right: 70px;
    top: 224px;
    text-align: right;
  }
  .person-name {
    color: var(--orange);
    font-size: 21px;
    letter-spacing: 0.5px;
    text-transform: uppercase;
  }
  .person-role { font-size: 16px; margin-top: 2px; }
  .band {
    position: absolute;
    left: 0;
    bottom: 0;
    width: 100%;
    height: 54px;
  }
</style>
</head>
<body>

<section class="card card-front" aria-label="Business card front">
  <span class="front-mark"></span>
  <h1 class="front-name">Bramble Bunnies</h1>
  <p class="front-web">www.Bramble-Bunnies.com</p>
</section>

<section class="card card-back" aria-label="Business card back">
  <div class="back-watermark"></div>

  <div class="brand">
    <span class="brand-mark"></span>
    <h2 class="brand-name">Bramble Bunnies</h2>
  </div>

  <ul class="contact-list">
    <li class="contact-item">
      <svg viewBox="0 0 24 24"><path d="M6.6 10.8a15 15 0 0 0 6.6 6.6l2.2-2.2c.3-.3.7-.4 1-.2 1.1.4 2.3.6 3.6.6.6 0 1 .4 1 1V20c0 .6-.4 1-1 1A17 17 0 0 1 3 4c0-.6.4-1 1-1h3.5c.6 0 1 .4 1 1 0 1.3.2 2.5.6 3.6.1.3 0 .7-.2 1z"/></svg>
      <span>9495817302</span>
    </li>
    <li class="contact-item">
      <svg viewBox="0 0 24 24"><path d="M2 5h20v14H2z M2 5l10 8 10-8" fill="none" stroke="#ef7d55" stroke-width="2.4"/></svg>
      <span>Info@Bramble-Bunnies.com</span>
    </li>
    <li class="contact-item">
      <svg viewBox="0 0 24 24"><circle cx="12" cy="12" r="10"/><path d="M2 12h20M12 2c3 3 3 17 0 20M12 2c-3 3-3 17 0 20" fill="none" stroke="#fff" stroke-width="1.4"/></svg>
      <span>www.Bramble-Bunnies.com</span>
    </li>
    <li class="contact-item">
      <svg viewBox="0 0 24 24"><path d="M12 2a7 7 0 0 0-7 7c0 5 7 13 7 13s7-8 7-13a7 7 0 0 0-7-7zm0 9.5A2.5 2.5 0 1 1 12 6.5a2.5 2.5 0 0 1 0 5z"/></svg>
      <span>20418 Wexley C #5127 Irvine Ca 92687</span>
    </li>
  </ul>

  <div class="person">
    <p class="person-name">Rosalind Hatchett</p>
    <p class="person-role">CEO</p>
  </div>

  <svg class="band" viewBox="0 0 700 54" preserveAspectRatio="none" aria-hidden="true">
    <rect x="0" y="6" width="700" height="48" fill="#ef7d55"/>
    <polygon points="555,0 700,0 700,54 545,54" fill="#8a4429"/>
    <polygon points="548,0 555,0 545,54 538,54" fill="#ffffff"/>
  </svg>
</section>

</body>
</html>
```